PSD Designs needed to give to my Developer

Hello, I need PSD files to give to my programmer for the creation of my new website. The website is for ZORVA lane, a new clothing company based in Chicago, IL. We sell womens, mens and kids fashion. We specialize in jackets, outerwear and sweaters, but we sell clothing from every category, I have someone working on the logo, so I can't include it for reference. However, I have included 2 reference sites as well as a PDF of how the 2 reference sites could be merged together. The main company color should be blue (hence the name ZORVA lane), and the overall feel of the site should be FUN. It should communicate: This is where you want to shop if you want a FUN, HAPPY experience. I need the Home Page file designed very quickly. Whoever is awarded this job will immediately continue working with me to design the other 8 pages. I will pay for all pages. The amount I am offering is for this one page only, and I will pay you additional to design all other 8 pages. Thank you for your time and I will be picking the best design so that we can immediately build a great relationship and work through the rest of the project.

Industry/Entity Type

Apparel Store

Number of Pages Required

1 page

Font styles to use
Sans Serif

Colors
33a6d7
0492cd
ffffff

Requirements
Must have
• I have included all notes in the project description so please check there. My project must communicate: Fun and Happy Design. Even tho I have chosen a few variations of blue below, I still want the designer to incorporate other colors as necessary to acheive the desired look.
Should not have
• It should have a boring, childish feel

```html
<!DOCTYPE html>
<html lang="en">
<head>
<meta charset="utf-8">
<title>ZORVA lane — Home</title>
<link rel="stylesheet" href="https://fonts.googleapis.com/css2?family=Arimo:wght@700&family=Six+Caps&display=swap">
<style>
  :root{
    --blue:#0b9ad0;
    --blue-bright:#33a6d7;
    --blue-deep:#0492cd;
    --blue-nav:#0a7fb0;
    --white:#ffffff;
    --page-wash-a:#eef6f7;
    --page-wash-b:#d4e7ea;
  }
  *{box-sizing:border-box;margin:0;padding:0}
  html,body{width:1200px;height:1000px;overflow:hidden}
  body{position:relative;font-family:"Arimo",Arial,sans-serif;font-weight:700;background:var(--page-wash-a)}
  .backdrop{position:absolute;inset:0;background:radial-gradient(ellipse at 50% 40%,#f8fbfb 0%,var(--page-wash-a) 45%,var(--page-wash-b) 100%)}

  .promo-bar{position:absolute;left:30px;top:17px;width:1138px;height:40px;background:var(--blue);color:var(--white)}
  .promo-text{position:absolute;left:11px;top:9px;font-size:20px}
  .stylist-login{position:absolute;left:796px;top:8px;font-size:19px;color:var(--white);text-decoration:none}
  .social{position:absolute;left:957px;top:5px;display:flex;gap:9px;list-style:none}
  .social li{width:30px;height:30px;border-radius:5px;background:var(--white)}

  .main-nav{position:absolute;left:32px;top:102px;display:flex;list-style:none;font-size:17px}
  .main-nav a{color:var(--blue-bright);text-decoration:none;margin-right:29px}
  .main-nav .current a{color:var(--blue-nav);margin-right:20px;display:inline-block;border-bottom:5px solid var(--blue-nav);padding-bottom:3px}

  .logo-slot{position:absolute;left:780px;top:75px;width:380px;text-align:center;color:var(--blue);font-size:43px;line-height:54px}

  .portrait{position:absolute;left:83px;top:140px;width:360px;height:356px;border-radius:50%;
    background:radial-gradient(circle at 50% 45%,#c08c58 0%,#a6774a 22%,#f3f3f3 40%,#ffffff 70%);
    box-shadow:0 0 28px 10px rgba(120,200,210,.55);border-bottom:5px solid var(--blue)}

  .hero{position:absolute;left:480px;top:213px;width:611px;height:235px;border-radius:8px;overflow:hidden;
    background:linear-gradient(100deg,#6f7a86 0%,#243e5e 30%,#1e3858 60%,#2e4866 100%);
    box-shadow:0 0 30px 8px rgba(150,215,225,.6)}
  .display{font-family:"Six Caps",sans-serif;font-weight:400;line-height:1;paint-order:stroke fill;white-space:nowrap;position:absolute}
  .hero-title{left:95px;top:-10px;font-size:196px;letter-spacing:0}
  .hero-title .outlined{color:var(--white);-webkit-text-stroke:4px var(--blue-deep)}
  .hero-title .filled{color:var(--blue-deep);-webkit-text-stroke:4px var(--white)}
  .hero-tagline{left:182px;top:188px;font-size:40px;color:var(--white);-webkit-text-stroke:3px var(--blue-deep);letter-spacing:3.5px}

  .slider-dots{position:absolute;left:578px;top:474px;display:flex;gap:10px;list-style:none}
  .slider-dots li{width:13px;height:13px;border-radius:50%;border:2px solid var(--blue-bright);background:var(--white)}
  .slider-dots li.active{background:radial-gradient(circle,var(--blue-bright) 0 3px,var(--white) 3.5px)}

  .tile{position:absolute;border-radius:8px;overflow:hidden;text-decoration:none;
    box-shadow:0 0 26px 6px rgba(150,215,225,.55)}
  .tile-label{color:var(--white);-webkit-text-stroke:3px var(--blue-deep)}
  .tile-story{left:23px;top:513px;width:577px;height:192px;
    background:linear-gradient(180deg,#2c3a58 0%,#b83c52 25%,#c86a78 45%,#6b6f60 70%,#8a8c86 100%)}
  .tile-shop{left:611px;top:513px;width:577px;height:192px;
    background:linear-gradient(160deg,#c9cfd4 0%,#a55a3a 20%,#3c4a66 50%,#7f8898 75%,#e6e6e4 100%)}
  .tile-story .tile-label,.tile-shop .tile-label{font-size:159px;letter-spacing:5px;top:18px}
  .tile-story .tile-label{left:54px}
  .tile-shop .tile-label{left:180px}
  .tile-join{left:23px;top:732px;width:1165px;height:190px;
    background:linear-gradient(90deg,#b6bcc2 0%,#2f3f50 25%,#8d6a58 45%,#3a4452 65%,#a08a70 85%,#f4f4f4 100%)}
  .tile-join .tile-label{font-size:121px;letter-spacing:4px;left:162px;top:57px}

  .footer-nav{position:absolute;left:0;top:941px;width:1200px;display:flex;justify-content:center;list-style:none;font-size:17px;padding-right:30px}
  .footer-nav a{color:var(--blue-deep);text-decoration:none;margin:0 14px}
  .copyright{position:absolute;left:0;top:970px;width:1200px;text-align:center;font-size:16px;color:var(--blue-deep);padding-left:18px}
</style>
</head>
<body>
  <div class="backdrop" role="img" aria-label="Softly blurred shopping arcade background"></div>

  <header>
    <div class="promo-bar">
      <p class="promo-text">Pop-up your own ZORVA Boulevard for ONLY $99</p>
      <a class="stylist-login" href="#">Stylist Login</a>
      <ul class="social" aria-label="Social links">
        <li aria-label="Social link"></li><li aria-label="Social link"></li><li aria-label="Social link"></li><li aria-label="Social link"></li>
      </ul>
    </div>
    <nav>
      <ul class="main-nav">
        <li class="current"><a href="#">HOME</a></li>
        <li><a href="#">GET TO KNOW US</a></li>
        <li><a href="#">WHY ZORVA?</a></li>
        <li><a href="#">HOST A POP-UP</a></li>
        <li><a href="#">BECOME A STYLIST</a></li>
      </ul>
    </nav>
    <div class="logo-slot">ZORVA lane logo<br>here</div>
  </header>

  <main>
    <div class="portrait" role="img" aria-label="Photo of a stylish man in a tan suede bomber jacket"></div>

    <section class="hero" role="img" aria-label="Close-up photo of a man in a blue checked suit jacket">
      <h1 class="display hero-title"><span class="outlined">MEN</span> <span class="filled">STYLING</span></h1>
      <p class="display hero-tagline">SHOP HERE LIKE A BOSS</p>
    </section>
    <ul class="slider-dots" aria-label="Slides">
      <li></li><li class="active"></li><li></li><li></li>
    </ul>

    <a class="tile tile-story" href="#" role="img" aria-label="Photo of folded knit sweaters"><span class="display tile-label">OUR STORY</span></a>
    <a class="tile tile-shop" href="#" role="img" aria-label="Photo of sweaters on wooden hangers"><span class="display tile-label">SHOP</span></a>
    <a class="tile tile-join" href="#" role="img" aria-label="Photo of three smiling friends in beanies"><span class="display tile-label">BE HAPPIER, JOIN THE MOUVEMENT</span></a>
  </main>

  <footer>
    <ul class="footer-nav">
      <li><a href="#">HOME</a></li>
      <li><a href="#">GET TO KNOW US</a></li>
      <li><a href="#">WHY ZORVA?</a></li>
      <li><a href="#">HOST A POP-UP</a></li>
      <li><a href="#">BECOME A STYLIST</a></li>
    </ul>
    <p class="copyright">© 2018 ZORVA lane Chicqgo IL. All Rights Reserve</p>
  </footer>
</body>
</html>
```